■サイトマップ
★:Gナビに掲載希望

TOP ★
写真館のこと ★
料金一覧 ★
店舗情報 ★
スタッフ紹介
ギャラリー ★
お子さまの成長の記念に(七五三)
思い出やこだわりにあわせた屋外撮影(ロケーション・出張撮影)
季節限定!キャンペーンフォト
キッズ・ベビー・お宮参りの撮影もおまかせください
成人の節目に晴れ姿を撮影
入園・入学・卒業
そのほかの撮影
よくある質問 ★
お問い合わせ(追従ボタン)
ブログ
ニュース

※お子さまの記念~そのほかの撮影のページ
「撮影のこだわり」という文言をGナビに配置して
プルダウンで表示させたいです。

■ターゲット
30~40代 主婦層にあわせて作る
店舗へ電話をかけてくるのはお母さんのため。

■TOPで目立たせたいコンテンツ
・季節限定!キャンペーンフォト
・思い出やこだわりにあわせた屋外撮影(ロケーション・出張撮影)

■上記以外でTOPに掲載したいコンテンツ
・ギャラリー
・写真館のこと
・七五三
・ブログ(更新頻度は低め)
・ニュース(更新頻度は低め)
・元気いっぱいなお子さまの撮影はお任せください!(リンクなし)
・スタッフ紹介

■デザインについて
・英語表記をする際は日本語表記もそえてください。
・Gナビを英語表記にする際は、オンカーソルで日本語表記が出るようにしてほしいです。
・子供の写真は幼稚園~小学校くらいの年齢をメインにしてください。
・キャンペーンページへの追従ボタンを配置。
・メインスライドは大きく、写真がよく見えるように。
・画像を大きめに載せたいです。

■デザイン参考サイト
http://moribana-kobo.jp/
業種やことなりますが、Gナビがおしゃれです。

https://www.lumelle-atelier.com/
シンプルで遊び心が感じられます。
手書き風のイラストがかわいいです。

https://www.tovimo.com/kids/
撮影メニュー・催事の項目で取り扱いプランの一覧がわかっていいです。

■フォントについて
WEB上で使用可能な無料のフォントで作成お願い致します。
OSに紐づくフォントの使用は控えていただければと思います。
(ヒラギノなど)

===============================
●ロゴ
https://hakobox-share.jp/download/7b1e9d2a6c3f85e0a4d71b6c9f02e58d3a1c7b4e
ダウンロードパスワード 7mwz3rpt

●素材
https://hakobox-share.jp/download/9e5c2b7f1a08d46c3e97b2f0d51a8c6e4b3f7d21
ダウンロードパスワード 7mwz3rpt
http://www.fh-taniyama.com/
1ページ
シンプル 複雑
単色 カラフル
暗い 明るい
日常 高級
遊び心 厳粛
未来的 伝統的
女性的 男性的
茶系、緑系、グレー系
• イラストレーター形式 (.ai)
• フォトショップ形式 (.psd)
• PNG形式 (.png)
◆文言について
現行サイトの文章を使用してOKです。

◆素材について
素材として必要なものがある場合には、Velmora Pics画像をご使用ください。
その際、通常アセットでダウンロード出来る画像のみを使用してください。
Velmora Pics以外の素材を使用する際には、
必ず無料で提供いただける物のみご使用ください。

◆注意
店舗へ直接の問い合わせはおやめください。
すでに案をご提出くださった方々、ご応募いただきありがとうございます。
せっかくですので開催期間を延長したいと思います。
何卒よろしくお願いいたします。

雰囲気がにぎやかすぎず渋すぎず、ちょうどよかったため。

この度は選定について大変お待たせいたしました。
また機会がありましたら何卒よろしくお願いいたします。

```html
<!DOCTYPE html>
<html lang="ja">
<head>
<meta charset="utf-8">
<title>ひなた写真館</title>
<link rel="stylesheet" href="https://fonts.googleapis.com/css2?family=Zen+Maru+Gothic:wght@400;500;700&family=Josefin+Sans:wght@300;400;600&display=swap">
<style>
:root{
  --brown:#a99078;
  --brown-dark:#7d6a58;
  --beige:#f4f0ea;
  --blush:#ede3dc;
  --ink:#5a4e44;
  --line:#d9cfc4;
  --white:#ffffff;
  --yellow:#f6e27a;
  --sky:#8fb3c9;
  --photo-warm:#c9b29a;
  --photo-green:#9aa58a;
  --photo-light:#e9e4dc;
}
*{box-sizing:border-box;margin:0;padding:0}
html,body{width:1200px;height:2613px;overflow:hidden}
body{font-family:"Zen Maru Gothic",sans-serif;color:var(--ink);background:var(--white);position:relative;font-size:14px}
.en{font-family:"Josefin Sans",sans-serif;letter-spacing:.12em}
.photo{display:block;background:linear-gradient(135deg,var(--photo-warm),var(--photo-green))}
.btn{display:block;width:240px;height:40px;margin:0 auto;background:var(--brown);color:var(--white);text-align:center;line-height:40px;font-size:13px;letter-spacing:.1em;border-radius:2px}
.sec-title{text-align:center}
.sec-title h2{font-size:24px;font-weight:500;letter-spacing:.15em}
.sec-title p{font-size:12px;color:var(--brown);margin-top:6px}

/* hero */
.hero{height:260px;display:flex;gap:8px}
.hero .slide{flex:1;position:relative}
.hero .slide-main{background:linear-gradient(120deg,#d8c7ad,#b7a58a 60%,#8c8a6e)}
.hero .slide-next{background:linear-gradient(120deg,#c8c08f,#a7a070 55%,#e2d9c0)}
.campaign-copy{position:absolute;left:80px;top:40px;color:var(--white);text-align:center}
.campaign-copy .tag{display:inline-block;background:var(--brown);padding:3px 12px;font-size:12px}
.campaign-copy h1{font-family:"Josefin Sans",sans-serif;font-size:46px;font-weight:300;letter-spacing:.18em;line-height:1.15;margin-top:8px}
.campaign-copy p{font-size:13px;margin-top:6px;letter-spacing:.1em}
.next-copy{position:absolute;left:100px;top:70px;color:var(--white);font-size:22px;line-height:1.6;letter-spacing:.12em}

/* header */
.site-header{height:52px;display:flex;align-items:center;padding:0 80px;border-bottom:1px solid var(--line)}
.logo{display:flex;align-items:center;gap:10px;font-size:22px;font-weight:700;letter-spacing:.12em;color:var(--ink)}
.logo i{width:14px;height:14px;border-radius:50%;background:var(--brown)}
.gnav{display:flex;gap:34px;margin-left:60px;font-size:13px;list-style:none}

/* about */
.about{height:278px;position:relative;background:linear-gradient(90deg,#f2efe9,#e7e1d8 60%,#f5f2ee)}
.about-card{position:absolute;left:50%;top:34px;transform:translateX(-50%);width:360px;height:210px;background:rgba(255,255,255,.88);padding:24px 36px;text-align:center}
.about-card h2{font-size:20px;font-weight:500;letter-spacing:.15em}
.about-card .en{font-size:11px;color:var(--brown)}
.about-card p{font-size:12px;line-height:1.9;margin:12px 0 14px;text-align:left}

/* follow */
.follow-tab{position:absolute;right:28px;top:420px;width:34px;height:120px;background:var(--white);border:1px solid var(--brown);color:var(--brown);writing-mode:vertical-rl;font-size:13px;letter-spacing:.2em;display:flex;align-items:center;justify-content:center;z-index:5}

/* menu */
.menu{height:470px;background:var(--beige);padding-top:36px}
.menu-grid{width:840px;margin:28px auto 0;display:grid;grid-template-columns:repeat(3,1fr);gap:20px 24px}
.menu-item .photo{height:140px}
.menu-item span{display:block;text-align:center;font-size:13px;margin-top:8px}

/* news */
.news{height:140px;display:flex;align-items:center;width:840px;margin:0 auto;gap:40px}
.news-head{width:150px;height:70px;border:1px solid var(--line);display:flex;align-items:center;justify-content:center;font-size:18px;letter-spacing:.15em}
.news-list{list-style:none;flex:1}
.news-list li{font-size:12px;padding:8px 0;border-bottom:1px dotted var(--line)}
.news-list time{color:var(--brown);margin-right:24px}

/* blog */
.blog{height:160px;display:flex;align-items:center;width:840px;margin:0 auto;gap:40px}
.blog-head{width:150px;font-size:18px;letter-spacing:.15em;text-align:center}
.blog-list{display:flex;gap:28px;flex:1}
.blog-card{flex:1;display:flex;gap:12px;align-items:center;font-size:12px;line-height:1.6}
.blog-card .photo{width:90px;height:80px;flex:none}

/* kids */
.kids{height:220px;position:relative;background:#fbf8ef;overflow:hidden}
.kids .photo{position:absolute;left:80px;top:20px;width:330px;height:180px;background:linear-gradient(135deg,#e8d6b6,#c6ad8c)}
.kids-copy{position:absolute;left:480px;top:48px}
.kids-copy h2{font-family:"Josefin Sans",sans-serif;font-size:62px;font-weight:300;color:var(--sky);letter-spacing:.15em;line-height:1}
.kids-copy p{display:inline-block;margin-top:18px;background:var(--yellow);padding:6px 18px;font-size:14px}

/* staff */
.staff{height:330px;background:var(--blush);padding-top:34px}
.staff-grid{width:840px;margin:26px auto 22px;display:grid;grid-template-columns:repeat(4,1fr);gap:24px}
.staff-card .photo{height:130px;background:linear-gradient(135deg,#d9cfc5,#b9a894)}
.staff-card span{display:block;background:var(--white);text-align:center;font-size:12px;padding:6px 0}

/* gallery */
.gallery{height:400px;padding-top:30px;position:relative}
.gallery-grid{width:840px;margin:24px auto 24px;display:grid;grid-template-columns:repeat(4,1fr);gap:10px}
.gallery-grid .photo{height:110px}
.page-top{position:absolute;right:90px;top:356px;width:32px;height:32px;border:1px solid var(--line);border-radius:50%;display:flex;align-items:center;justify-content:center}

/* footer */
.site-footer{height:250px;background:#f7f6f3;display:flex;padding:40px 80px;gap:60px}
.footer-info{width:440px}
.footer-info .logo{font-size:28px}
.footer-info .tel{display:flex;align-items:center;gap:8px;font-size:20px;margin-top:20px}
.footer-info address{font-style:normal;font-size:12px;line-height:1.8;margin-top:8px}
.social{display:flex;gap:10px;margin-top:14px}
.social i{width:22px;height:22px;border-radius:50%;background:var(--brown)}
.map{flex:1;height:170px;background:linear-gradient(135deg,#eceae5,#d9d6cf)}

.bottom-bar{height:53px;background:var(--brown);color:var(--white);display:flex;flex-direction:column;align-items:center;justify-content:center;gap:6px}
.bottom-bar ul{list-style:none;display:flex;gap:30px;font-size:12px}
.bottom-bar small{font-size:10px;letter-spacing:.1em}
</style>
</head>
<body>

<section class="hero">
  <div class="slide slide-main" role="img" aria-label="キャンペーンフォト:笑顔の女の子と姉妹の屋外写真">
    <div class="campaign-copy">
      <span class="tag">季節限定</span>
      <h1>CAMPAIGN<br>PHOTO</h1>
      <p>季節限定!キャンペーンフォト</p>
    </div>
  </div>
  <div class="slide slide-next" role="img" aria-label="紅葉の中で親子を撮影した屋外ロケーション写真">
    <p class="next-copy">思い出やこだわりに<br>あわせた屋外撮影</p>
  </div>
</section>

<header class="site-header">
  <div class="logo"><i></i>ひなた写真館</div>
  <ul class="gnav">
    <li>写真館のこと</li><li>撮影のこだわり</li><li>料金</li><li>店舗情報</li><li>ギャラリー</li><li>よくある質問</li>
  </ul>
</header>

<section class="about" role="img" aria-label="白い光が差し込むスタジオ内観の写真">
  <div class="about-card">
    <h2>ひなた写真館のこと</h2>
    <span class="en">ABOUT</span>
    <p>お子さまの成長やご家族の大切な瞬間を、<br>自然な笑顔とともに一枚に残します。<br>ゆったりとしたスタジオで、のびのびと<br>撮影をお楽しみください。</p>
    <span class="btn">写真館のこと</span>
  </div>
</section>

<a class="follow-tab">キャンペーン</a>

<section class="menu">
  <div class="sec-title"><h2>撮影メニュー</h2><p class="en">MENU</p></div>
  <div class="menu-grid">
    <div class="menu-item"><span class="photo" role="img" aria-label="着物姿の七五三の写真"></span><span>七五三撮影</span></div>
    <div class="menu-item"><span class="photo" role="img" aria-label="屋外での家族写真"></span><span>ロケーション・出張撮影</span></div>
    <div class="menu-item"><span class="photo" role="img" aria-label="季節のキャンペーン写真"></span><span>キャンペーンフォト撮影</span></div>
    <div class="menu-item"><span class="photo" role="img" aria-label="キッズとベビーの写真"></span><span>キッズ・ベビー・お宮参り撮影</span></div>
    <div class="menu-item"><span class="photo" role="img" aria-label="成人式の振袖写真"></span><span>成人の節目撮影</span></div>
    <div class="menu-item"><span class="photo" role="img" aria-label="入学記念の写真"></span><span>入園・入学・卒業記念撮影</span></div>
  </div>
</section>

<section class="news">
  <div class="news-head">お知らせ</div>
  <ul class="news-list">
    <li><time>2020.10.01</time>秋のキャンペーンを開始しました</li>
    <li><time>2020.09.15</time>七五三撮影のご予約を受付中です</li>
    <li><time>2020.08.20</time>定休日変更のお知らせ</li>
  </ul>
</section>

<section class="blog">
  <div class="blog-head">ブログ</div>
  <div class="blog-list">
    <div class="blog-card"><span class="photo" role="img" aria-label="ブログ記事の写真"></span><p>秋の七五三撮影レポート</p></div>
    <div class="blog-card"><span class="photo" role="img" aria-label="ブログ記事の写真"></span><p>公園でのロケ撮影</p></div>
    <div class="blog-card"><span class="photo" role="img" aria-label="ブログ記事の写真"></span><p>新しい衣装が届きました</p></div>
  </div>
</section>

<section class="kids">
  <span class="photo" role="img" aria-label="元気に跳ねる子どもたちの写真"></span>
  <div class="kids-copy">
    <h2>KIDS PHOTO</h2>
    <p>元気いっぱいなお子さまの撮影はお任せください!</p>
  </div>
</section>

<section class="staff">
  <div class="sec-title"><h2>スタッフ紹介</h2><p class="en">STAFF</p></div>
  <div class="staff-grid">
    <div class="staff-card"><span class="photo" role="img" aria-label="スタッフの写真"></span><span>撮影担当 山田</span></div>
    <div class="staff-card"><span class="photo" role="img" aria-label="スタッフの写真"></span><span>着付担当 佐藤</span></div>
    <div class="staff-card"><span class="photo" role="img" aria-label="スタッフの写真"></span><span>撮影担当 中村</span></div>
    <div class="staff-card"><span class="photo" role="img" aria-label="スタッフの写真"></span><span>受付担当 小林</span></div>
  </div>
  <span class="btn">スタッフ紹介</span>
</section>

<section class="gallery">
  <div class="sec-title"><h2>ギャラリー</h2><p class="en">GALLERY</p></div>
  <div class="gallery-grid">
    <span class="photo" role="img" aria-label="ギャラリー写真"></span>
    <span class="photo" role="img" aria-label="ギャラリー写真"></span>
    <span class="photo" role="img" aria-label="ギャラリー写真"></span>
    <span class="photo" role="img" aria-label="ギャラリー写真"></span>
    <span class="photo" role="img" aria-label="ギャラリー写真"></span>
    <span class="photo" role="img" aria-label="ギャラリー写真"></span>
    <span class="photo" role="img" aria-label="ギャラリー写真"></span>
    <span class="photo" role="img" aria-label="ギャラリー写真"></span>
  </div>
  <span class="btn">ギャラリー一覧</span>
  <a class="page-top" aria-label="ページ上部へ">
    <svg width="12" height="8" viewBox="0 0 12 8"><path d="M1 7 6 2l5 5" fill="none" stroke="#a99078" stroke-width="1.5"/></svg>
  </a>
</section>

<footer class="site-footer">
  <div class="footer-info">
    <div class="logo"><i></i>ひなた写真館</div>
    <p class="tel">
      <svg width="18" height="18" viewBox="0 0 24 24"><path d="M6.6 10.8a15 15 0 0 0 6.6 6.6l2.2-2.2c.3-.3.7-.4 1-.2 1.1.4 2.3.6 3.6.6.6 0 1 .4 1 1V20c0 .6-.4 1-1 1A17 17 0 0 1 3 4c0-.6.4-1 1-1h3.5c.6 0 1 .4 1 1 0 1.3.2 2.5.6 3.6.1.3 0 .7-.2 1z" fill="#a99078"/></svg>
      <span class="en">012-345-6789</span>
    </p>
    <address>〒000-0000 みどり市中央町1-2-3<br>営業時間 10:00〜18:00 定休日 水曜日</address>
    <div class="social"><i></i><i></i><i></i></div>
  </div>
  <div class="map" role="img" aria-label="写真館周辺の地図"></div>
</footer>

<div class="bottom-bar">
  <ul><li>写真館のこと</li><li>撮影のこだわり</li><li>料金</li><li>店舗情報</li><li>ギャラリー</li><li>よくある質問</li><li>お問い合わせ</li></ul>
  <small class="en">© HINATA PHOTO STUDIO</small>
</div>

</body>
</html>
```